Poster Design Project for an Old-fashioned Ice Cream Parlor

We are an old-fashioned American ice cream company called Bemick's Ice Cream based in the San Francisco Bay Area. We would like a poster design to be put up on display in our parlors. The design should embody the American 1950s retro/vintage look that our company already identifies with, but spruced up with a modern touch. Feel free to be as creative as you like and remix it with your own style! There will be 3 winners and we are hoping for a variety of styles. Each winner will be rewarded with $130. We look forward to seeing your work!
Updates

Hello all,

In reply to some comments, I have uploaded our logo under the 'brief'. Our company was established in 1950. 

Industry/Entity Type

It Company

Requirements
Must have
• the 3 final posters we will select must be formatted to 18x22 inches
designs that incorporate pink, blue, and yellow (our brand colors) will be more likely to win; these colors do not have to be a major part of the artwork
Nice to have
• include the colors pink, blue, and yellow
Should not have
• designs should not be dark in theme

```html
<!DOCTYPE html>
<html lang="en">
<head>
<meta charset="utf-8">
<title>Bemick's Ice Cream — This Is How Ice Cream Used To And Should Be</title>
<link rel="stylesheet" href="https://fonts.googleapis.com/css2?family=Bungee+Inline&family=Chewy&family=Bowlby+One&family=Playfair+Display:wght@400&family=Salsa&family=Poppins:wght@600&display=swap">
<style>
  :root {
    --frame-blue: #7fc9d8;
    --parlor-pink: #f28aa7;
    --scoop-cream: #f3e4bd;
    --scoop-shade: #e9d3a8;
    --berry: #7c2f4c;
    --caramel: #9b6b3a;
    --toffee: #c8a26b;
    --vanilla: #f6ecd2;
    --canvas-w: 981px;
    --canvas-h: 1200px;
  }
  * { box-sizing: border-box; margin: 0; padding: 0; }
  html, body {
    width: var(--canvas-w);
    height: var(--canvas-h);
    overflow: hidden;
    background: var(--frame-blue);
  }
  .poster {
    position: relative;
    width: var(--canvas-w);
    height: var(--canvas-h);
    background: var(--frame-blue);
  }
  .poster__field {
    position: absolute;
    left: 40px;
    top: 40px;
    width: 901px;
    height: 1120px;
    background: var(--parlor-pink);
  }
  .scoop {
    position: absolute;
    left: 217px;
    top: 73px;
    width: 543px;
    height: 420px;
  }
  .headline {
    position: absolute;
    left: 0;
    width: var(--canvas-w);
    text-align: center;
    line-height: 1;
  }
  .headline--this-is-how {
    top: 505px;
    font-family: "Bungee Inline", sans-serif;
    font-size: 78px;
    color: var(--berry);
    letter-spacing: 1px;
  }
  .headline--ice-cream {
    top: 598px;
    font-family: "Chewy", sans-serif;
    font-size: 74px;
    color: var(--caramel);
  }
  .headline--used-to {
    top: 690px;
    display: flex;
    justify-content: center;
    gap: 6px;
  }
  .block-letter {
    display: inline-block;
    width: 50px;
    height: 66px;
    background: var(--berry);
    transform: skewY(-6deg);
    font-family: "Bowlby One", sans-serif;
    font-size: 46px;
    line-height: 66px;
    color: var(--vanilla);
    text-align: center;
  }
  .block-letter span { display: inline-block; transform: skewY(6deg); }
  .block-gap { width: 30px; }
  .headline--and {
    top: 776px;
    display: flex;
    justify-content: center;
    gap: 0;
  }
  .oval-letter {
    width: 76px;
    height: 98px;
    margin: 0 -2px;
    border-radius: 50%;
    background: var(--toffee);
    border: 2px solid var(--berry);
    font-family: "Playfair Display", serif;
    font-size: 60px;
    line-height: 94px;
    color: var(--vanilla);
    text-align: center;
  }
  .headline--should {
    top: 872px;
    font-family: "Salsa", cursive;
    font-size: 84px;
    color: var(--caramel);
  }
  .headline--be {
    top: 968px;
    font-family: "Poppins", sans-serif;
    font-weight: 600;
    font-size: 78px;
    color: var(--berry);
  }
  .brand-name {
    position: absolute;
    left: 742px;
    top: 1022px;
    display: flex;
    align-items: center;
    gap: 10px;
    font-family: "Chewy", sans-serif;
    font-size: 38px;
    color: var(--berry);
  }
  .brand-name__dot {
    width: 22px;
    height: 22px;
    border-radius: 50%;
    background: var(--vanilla);
  }
</style>
</head>
<body>
  <main class="poster">
    <div class="poster__field"></div>

    <svg class="scoop" role="img" aria-label="Illustration of a melting scoop of vanilla ice cream" viewBox="0 0 543 420">
      <ellipse cx="271" cy="200" rx="270" ry="190" fill="var(--scoop-cream)"/>
    </svg>

    <h1 class="headline headline--this-is-how">THIS IS HOW</h1>
    <p class="headline headline--ice-cream">ice cream</p>
    <p class="headline headline--used-to" aria-label="used to">
      <span class="block-letter"><span>U</span></span>
      <span class="block-letter"><span>S</span></span>
      <span class="block-letter"><span>E</span></span>
      <span class="block-letter"><span>D</span></span>
      <span class="block-gap"></span>
      <span class="block-letter"><span>T</span></span>
      <span class="block-letter"><span>O</span></span>
    </p>
    <p class="headline headline--and" aria-label="and">
      <span class="oval-letter">A</span>
      <span class="oval-letter">N</span>
      <span class="oval-letter">D</span>
    </p>
    <p class="headline headline--should">should</p>
    <p class="headline headline--be">be</p>

    <div class="brand-name">
      <span class="brand-name__dot"></span>
      <span>Bemick's</span>
    </div>
  </main>
</body>
</html>
```